Make the invisible visible.... and attractive

I have an online course at http://www.brightlanepath.com/Begin-today-here.html. I need an attractive graphic to sell the product. The course is a series of video, audio and handout materials set out in 32 lessons and has a free one year confidence course as a bonus.

Target Market(s)

Individuals who have problems with fear or anxiety.

Industry/Entity Type

Audio

```html
<!DOCTYPE html>
<html lang="en">
<head>
<meta charset="utf-8">
<title>Brightlane Course – Home</title>
<link rel="stylesheet" href="https://fonts.googleapis.com/css2?family=Arimo:wght@400;700&family=Montserrat:wght@300;400&family=Kalam:wght@400&display=swap">
<style>
  :root {
    --topbar: #333333;
    --header-bg: #f7f7f7;
    --green: #7d9a3a;
    --green-dark: #6b8a2e;
    --nav-sub: #8a8a8a;
    --text: #333333;
    --muted: #666666;
    --navy: #1a1f8f;
    --button: #1408b8;
    --line: #e2e2e2;
    --white: #ffffff;
  }
  * { box-sizing: border-box; margin: 0; padding: 0; }
  html, body { width: 1200px; height: 601px; overflow: hidden; background: var(--white); font-family: "Arimo", Arial, sans-serif; color: var(--text); }
  .page { position: relative; width: 1200px; height: 601px; overflow: hidden; }

  .topbar { position: absolute; left: 0; top: 0; width: 1200px; height: 9px; background: var(--topbar); }
  .topbar .active-tab { position: absolute; left: 332px; width: 104px; height: 12px; background: var(--green); }
  .topbar .active-tab::after { content: ""; position: absolute; left: 46px; bottom: -6px; border: 6px solid transparent; border-top-color: var(--green); border-bottom: 0; }

  .site-header { position: absolute; left: 0; top: 9px; width: 1200px; height: 92px; background: linear-gradient(#ffffff, var(--header-bg)); border-bottom: 1px solid var(--line); }
  .brand { position: absolute; left: 104px; top: 30px; display: flex; align-items: center; gap: 10px; }
  .brand-mark { width: 26px; height: 26px; border-radius: 50%; background: var(--green); }
  .brand-name { font-family: "Arimo", Arial, sans-serif; font-weight: 700; font-size: 21px; line-height: 26px; color: var(--green); }
  .divider { position: absolute; left: 331px; top: 8px; height: 82px; border-left: 1px dotted #bbbbbb; }

  .main-nav { position: absolute; left: 347px; top: 22px; display: flex; }
  .main-nav a { display: block; width: 104px; text-decoration: none; }
  .main-nav .label { display: block; font-size: 14px; color: var(--green); line-height: 18px; }
  .main-nav .sub { display: block; font-size: 11px; color: var(--nav-sub); line-height: 14px; margin-top: 5px; }
  .main-nav a.current .label { font-weight: 700; color: var(--green-dark); }

  .hero { position: absolute; left: 88px; top: 119px; width: 711px; height: 256px; border: 1px solid #bbbbbb; overflow: hidden; background: var(--white); }
  .hero svg.backdrop { position: absolute; left: 0; top: 0; }
  .hero .photo { position: absolute; left: 478px; top: 0; width: 233px; height: 256px; background: linear-gradient(100deg, rgba(238,248,252,0) 0%, #d9b49c 30%, #b07e62 55%, #6e4534 80%, #e8f5fb 100%); }
  .hero .title { position: absolute; left: 18px; top: 24px; font-family: "Montserrat", sans-serif; font-weight: 300; color: var(--white); font-size: 50px; line-height: 50px; }
  .hero .rule { position: absolute; left: 25px; width: 164px; border-top: 1px solid rgba(255,255,255,0.8); }
  .hero .lessons { position: absolute; left: 25px; top: 148px; width: 164px; text-align: center; font-family: "Montserrat", sans-serif; font-size: 19px; letter-spacing: 3px; line-height: 25px; color: #eef6d8; }
  .hero .bonus { position: absolute; left: 18px; top: 226px; font-family: "Kalam", cursive; font-size: 13px; color: var(--white); }
  .hero .headline { position: absolute; left: 257px; top: 16px; font-family: "Montserrat", sans-serif; color: var(--navy); font-size: 31px; line-height: 36px; }
  .hero .headline small { font-size: 27px; }
  .hero .lead { position: absolute; left: 265px; top: 130px; font-family: "Montserrat", sans-serif; font-size: 14px; line-height: 23px; color: #444; text-align: center; width: 200px; }
  .hero .cta { position: absolute; left: 282px; top: 194px; width: 185px; height: 43px; border-radius: 7px; background: var(--button); color: var(--white); font-family: "Montserrat", sans-serif; font-size: 18px; line-height: 43px; text-align: center; text-decoration: none; }

  .intro-title { position: absolute; left: 99px; top: 395px; width: 690px; font-size: 26px; font-weight: 700; line-height: 33px; color: var(--text); }
  .article-tools { position: absolute; left: 723px; top: 502px; display: flex; gap: 8px; }

  .sidebar-box { position: absolute; left: 832px; width: 243px; background: var(--white); border: 1px solid var(--line); border-radius: 4px; }
  .call-box { top: 132px; height: 124px; text-align: center; }
  .call-box h2 { margin-top: 8px; font-size: 24px; color: var(--green); font-weight: 700; }
  .call-box .phone { margin-top: 22px; font-size: 24px; font-weight: 700; color: #555; }

  .promo { position: absolute; left: 803px; top: 488px; width: 397px; height: 113px; border: 2px solid #2b3a12; background: linear-gradient(110deg, #3a2a22 0%, #3a2a22 8%, #8cbf3a 20%, #a6d14b 60%, #5aa0d8 100%); }

  .help-box { top: 370px; height: 240px; z-index: 2; }
  .help-box h2 { font-size: 16px; font-weight: 700; color: var(--text); padding: 9px 14px; border-bottom: 1px solid var(--line); }
  .help-box p { padding: 12px 36px 0 14px; font-size: 13.4px; line-height: 21.6px; color: var(--muted); }
  .help-box input { display: block; margin: 12px 0 0 22px; width: 150px; height: 22px; border: 1px solid #c8c8c8; font: 13px "Arimo", Arial, sans-serif; padding: 0 4px; color: #444; }
  .help-box input + input { margin-top: 8px; }
</style>
</head>
<body>
<div class="page">
  <div class="topbar"><div class="active-tab"></div></div>

  <header class="site-header">
    <div class="brand">
      <div class="brand-mark"></div>
      <div class="brand-name">Brightlane Course</div>
    </div>
    <div class="divider"></div>
    <nav class="main-nav">
      <a class="current" href="#"><span class="label">HOME</span><span class="sub">Home</span></a>
      <a href="#"><span class="label">ONLINE</span><span class="sub">Course</span></a>
      <a href="#"><span class="label">WHY</span><span class="sub">Do the course</span></a>
      <a href="#"><span class="label">Where</span><span class="sub">and prices</span></a>
      <a href="#"><span class="label">FAQ</span><span class="sub">Questions<br>Answered</span></a>
      <a href="#"><span class="label">Terms</span><span class="sub">&amp; conditions</span></a>
      <a href="#"><span class="label">Contact</span><span class="sub">us</span></a>
    </nav>
  </header>

  <section class="hero">
    <svg class="backdrop" width="711" height="256" viewBox="0 0 711 256">
      <defs>
        <linearGradient id="sky" x1="0" x2="1">
          <stop offset="0" stop-color="#a9e1f5"/>
          <stop offset="0.35" stop-color="#e6f6fc"/>
          <stop offset="1" stop-color="#f5fbfe"/>
        </linearGradient>
      </defs>
      <rect width="711" height="256" fill="url(#sky)"/>
      <path d="M0 0 H232 C196 60 196 190 250 256 H0 Z" fill="#7e9a3d"/>
      <path d="M232 0 C196 60 196 190 250 256" fill="none" stroke="#5fcbee" stroke-width="6" opacity="0.6"/>
    </svg>
    <div class="photo" role="img" aria-label="Photo of a relaxed woman with eyes closed, calm expression"></div>
    <div class="title">CALM<br>Course</div>
    <div class="rule" style="top:140px"></div>
    <div class="lessons">SET OUT IN<br>32 LESSONS</div>
    <div class="rule" style="top:201px"></div>
    <div class="bonus">Free 1 year confidence course</div>
    <div class="headline">Be calm and<br>composed<br><small>in any situation</small></div>
    <div class="lead">Develop powerful emotional resilience quickly and easily</div>
    <a class="cta" href="http://www.brightlanepath.com/Begin-today-here.html">Start Right Now</a>
  </section>

  <h1 class="intro-title">An introduction to the Brightlane Course and a free gift for you</h1>
  <div class="article-tools">
    <svg width="16" height="12" viewBox="0 0 16 12" aria-label="Email"><rect x="0.5" y="0.5" width="15" height="11" fill="#e8eef6" stroke="#667"/><path d="M1 1 L8 7 L15 1" fill="none" stroke="#667"/></svg>
    <svg width="16" height="14" viewBox="0 0 16 14" aria-label="Print"><rect x="4" y="0.5" width="8" height="5" fill="#fff" stroke="#555"/><rect x="0.5" y="5" width="15" height="6" fill="#999" stroke="#555"/><rect x="4" y="9" width="8" height="4.5" fill="#fff" stroke="#555"/></svg>
  </div>

  <aside class="sidebar-box call-box">
    <h2>Call us now</h2>
    <div class="phone">020 7946 0321</div>
  </aside>

  <div class="promo" role="img" aria-label="Promotional course banner with presenter photo and colourful graphics"></div>

  <aside class="sidebar-box help-box">
    <h2>Free Help and Advice</h2>
    <p>Get FREE help and advice for dealing with fears and anxieties. Just leave your first name and email and I will send you a complete series of resources and some of the very latest advice.</p>
    <input type="text" value="First Name" aria-label="First name">
    <input type="text" value="" aria-label="Email">
  </aside>
</div>
</body>
</html>
```